Molveta - Customer Experience Software Company Web Design

*****UPDATE*****
We've been getting a lot of corporate designs through. Unfortunately this is not what we are looking for. We would like our brand to be more approachable and for the look and feel to to be a bit more fun.
Also the best designs we have received so far have followed the "less is more" approach. Im hoping any news designs will take these aspects into account.
*****************

Background:

Molveta is a Customer Experience Technology company. We equip business and technology teams with the frameworks, tools and services to help them create compelling experiences for their customers.

Our flagship product - Molveta CX is an open-source customer experience application framework – it enables organisation to build highly differentiated business applications to deliver compelling experiences to your customers.

Molveta CX is designed for innovators who understand that unlocking opportunity in today’s competitive marketplace is driven by delivering a better customer experience.

Task:

We are looking for a web design (we need PSD, no HTML/CSS) for our company site through which to launch our customer experience framework product. The site will be also used as a support site, so the functional aspect of the site is as important as the visual impact for sales.

In order to help us conceptualise ideas and content we have drafted a temporary website using a standard wordpress theme (please see details below). Now we have a general idea of our requirements we like we would like to take it to the next level and get some designs with that professional edge.

Our target market are Enterprise organisations - that is senior members of the business & technology teams (Business General Managers, CTO’s, CIO’s, and Senior Architects and Senior Developers). We want something clean & fresh which is DIFFERENT from the typical corporate technology websites out there. We would like to be seen as more approachable than most large technology companies.

Words we would like to use to describe the finished design:
• Clean (we’re thinking white background with one or two key colours)
• Fresh
• Light
• Modern
• Less is more
• Web 2.0
• Fun but professional (aimed at Enterprise/Large organisations)
• Bold, clear call to action – e.g. Live Demo & Download
• Readable (but Sans Serif)

As we’re a Customer Experience company, the usability of the site is critical. The site must be functional, intuitive & easy to navigate. We want to keep the number of user clicks to the bare minimum possible.

Other aspects, which we would like to incorporate into the site
• Home Page banner slider
• Client logon
• Newsletter sign up
• Social media links – Friendloop, Careerweave (for starters)
• Rich footer links

Some websites we like
• http://brightpanelworks.com - clean, light, modern & intuitive
• http://www.tamsinvoroley.com - bold, clear messaging
• http://www.qz5.net/html/logo - punchy, colourful
• http://parcelwren.com/ - modern, clear messaging, colourful, rich footer area

Target Market(s)

Enterprise organisations - that is senior members of the business & technology teams (Business General Managers, CTO’s, CIO’s, Senior Devs)

Industry/Entity Type

Business

Requirements
Must have
• - Design Specs: Accepted file formats: During the design phase adobe PSD or JPEG are OK (if you need to upload files), but for the handover we'll need PSD only with all the original layers.
- The width needs to be a size that will work with every size computer screen
- Need to use cross-platform compatible font
- The graphic elements used for the design must be copyright free

Current test site
- URL http://molveta.com/wp-admin
- username: artfolkhub
- password: artfolkhub

IMPORTANT NOTE REGARDING OUR CURRENT TEST SITE:

This is a very basic version of a site to help us generate requirements. This design is only a starting point/input and is not locked in stone i.e. we do not simply want this site simply tweaked around the edges.

We are looking for you to use all of your graphic design skills and experience to create a truly awesome site design!

```html
<!DOCTYPE html>
<html lang="en">
<head>
<meta charset="utf-8">
<title>Molveta – The Customer Experience Framework</title>
<link rel="stylesheet" href="https://fonts.googleapis.com/css2?family=Ubuntu:wght@300;400&family=Roboto+Condensed:wght@300;400&family=Arimo&display=swap">
<style>
:root{
  --brand-red:#e0303a;
  --cta-top:#f35b4a;
  --cta-bottom:#e2332f;
  --page:#f5f5f3;
  --band:#cbcbcb;
  --ink:#444;
  --ink-soft:#666;
  --panel:#ffffff;
  --base:#333333;
  --btn-top:#f1f1f1;
  --btn-bottom:#b9b9b9;
  --screen:#222222;
  --icon:#f2f2f2;
}
*{margin:0;padding:0;box-sizing:border-box}
html,body{width:1200px;height:1029px;overflow:hidden;background:var(--page)}
body{position:relative;font-family:"Ubuntu",sans-serif;color:var(--ink)}
a{color:inherit;text-decoration:none}
ul{list-style:none}
h1,h2{font-weight:400}
.abs{position:absolute}
.condensed{font-family:"Roboto Condensed",sans-serif}

/* header */
.site-header{position:absolute;left:0;top:0;width:1200px;height:112px;background:var(--page)}
.brand-name{left:221px;top:18px;font-size:56px;font-weight:300;color:var(--brand-red);line-height:1;letter-spacing:-1px}
.brand-tagline{left:223px;top:74px;font-size:14px;color:var(--ink)}
.account-links{left:891px;top:23px;font-size:10px;line-height:12px;color:var(--ink);border-bottom:1px solid #999;padding-bottom:3px;word-spacing:2px}
.main-nav{right:219px;top:71px;display:flex;gap:22px;font-size:15.5px;color:var(--ink-soft)}

/* hero */
.hero{position:absolute;left:0;top:112px;width:1200px;height:380px;background:var(--band)}
.hero-title{left:223px;top:60px;font-weight:300;font-size:66px;line-height:74px;color:var(--ink)}
.hero-sub{left:224px;top:206px;font-family:"Roboto Condensed",sans-serif;font-weight:300;font-size:43px;line-height:50px;color:var(--ink)}
.cta{display:inline-flex;align-items:center;justify-content:center;color:#fff;background:linear-gradient(var(--cta-top),var(--cta-bottom));border-radius:4px;font-family:"Roboto Condensed",sans-serif}
.hero-cta{left:224px;top:278px;width:128px;height:39px;font-size:21px}
.slide-arrow{top:144px}
.slide-arrow.prev{left:158px}
.slide-arrow.next{left:1015px}
.product-visual{left:617px;top:45px;width:364px;height:332px;border-radius:8px 8px 4px 4px;background:linear-gradient(var(--screen) 0,var(--screen) 67%,#bdbdbd 67%,#e2e2e2 100%)}

/* intro */
.intro-heading{left:222px;top:539px;font-size:27.5px;line-height:32px;color:var(--ink)}
.intro-text{left:223px;top:618px;width:516px;font-family:"Arimo",sans-serif;font-size:13px;line-height:16.7px;color:var(--ink-soft)}
.btn{display:inline-flex;align-items:center;justify-content:center;font-family:"Roboto Condensed",sans-serif;font-size:14px;color:var(--ink);background:linear-gradient(var(--btn-top),var(--btn-bottom));border-radius:2px;height:28px}
.read-more{left:219px;top:748px;width:95px}
.product-panel{left:767px;top:525px;width:216px;height:267px;background:var(--panel);border-radius:4px}
.product-panel p{position:absolute;left:21px;top:21px;width:184px;font-size:15.5px;line-height:22.2px;font-weight:300;color:#333;letter-spacing:.3px}
.product-panel .btn-download{left:17px;top:223px;width:80px}
.product-panel .btn-demo{left:119px;top:223px;width:80px}

/* footer */
.site-footer{position:absolute;left:0;top:821px;width:1200px;height:171px;background:var(--band)}
.footer-list li{font-size:11px;line-height:21.8px;padding-left:16px;position:relative;color:#333}
.footer-list li::before{content:"";position:absolute;left:0;top:8px;width:5px;height:5px;border-radius:50%;background:#333}
.footer-heading{font-size:19.5px;color:var(--ink);line-height:1}
.nav-col{left:215px;top:28px}
.col-start{left:320px;top:36px}
.col-support{left:511px;top:36px}
.col-follow{left:640px;top:36px}
.col-news{left:800px;top:36px}
.footer-sub{margin-top:10px}
.footer-sub li::before{left:2px}
.social-links{display:flex;gap:8px;margin-top:13px}
.social-links a{width:25px;height:25px;background:var(--icon);border-radius:4px;box-shadow:inset 0 -2px 0 #c4c4c4}
.email-field{left:802px;top:69px;width:182px;height:31px;background:#e7e7e7;border-radius:3px;font-size:12.5px;color:#333;padding:9px 13px}
.signup{left:890px;top:112px;width:93px;height:28px;font-size:15px}
.legal-bar{position:absolute;left:0;top:992px;width:1200px;height:37px;background:var(--base);color:#eee;font-size:10.5px;padding:11px 0 0 215px;word-spacing:2px}
</style>
</head>
<body>

<header class="site-header">
  <div class="abs brand-name">Molveta</div>
  <div class="abs brand-tagline">The Customer Experience Framework</div>
  <div class="abs account-links"><a href="#">LOGIN</a> &nbsp;| &nbsp;<a href="#">REGISTER</a></div>
  <nav class="abs main-nav">
    <a href="#">Home</a><a href="#">Products</a><a href="#">Support</a><a href="#">Blog</a><a href="#">About</a><a href="#">Contact</a>
  </nav>
</header>

<section class="hero">
  <h1 class="abs hero-title">Customer<br>Experience</h1>
  <div class="abs hero-sub">Application Framework</div>
  <a class="abs cta hero-cta" href="#">LIVE DEMO</a>
  <svg class="abs slide-arrow prev" width="26" height="40" viewBox="0 0 26 40" aria-label="Previous slide"><polyline points="24,2 2,20 24,38" fill="none" stroke="#777" stroke-width="1.5"/></svg>
  <svg class="abs slide-arrow next" width="26" height="40" viewBox="0 0 26 40" aria-label="Next slide"><polyline points="2,2 24,20 2,38" fill="none" stroke="#777" stroke-width="1.5"/></svg>
  <div class="abs product-visual" role="img" aria-label="Desktop monitor displaying the Molveta CX analytics dashboard with bar, donut and funnel charts"></div>
</section>

<main>
  <h2 class="abs intro-heading">Create compelling experiences<br>for your customers</h2>
  <p class="abs intro-text">“Sed ut perspiciatis unde omnis iste natus error sit voluptatem accusantium doloremque laudantium, totam rem aperiam, eaque ipsa quae ab illo inventore veritatis et quasi architecto beatae vitae dicta sunt explicabo. Nemo enim ipsam voluptatem quia voluptas sit aspernatur aut odit aut fugit, sed quia consequuntur magni dolores eos qui ratione voluptatem sequi nesciunt. Neque porro quisquam est, qui dolorem ipsum quia dolor sit amet, consectetur, adipisci velit, sed quia non numquam eius modi tempora incidunt ut labore et dolore magnam aliquam quaerat voluptatem. Ut enim ad minima veniam, quis.</p>
  <a class="abs btn read-more" href="#">Read More</a>

  <aside class="abs product-panel">
    <p>Molveta CX is a customer experience application framework - it enables you to build highly differentiated business applications to deliver compelling experiences to your customers</p>
    <a class="abs btn btn-download" href="#">Download</a>
    <a class="abs btn btn-demo" href="#">Live Demo</a>
  </aside>
</main>

<footer class="site-footer">
  <ul class="abs footer-list nav-col">
    <li>Home</li><li>Products</li><li>Support</li><li>Blog</li><li>About</li><li>Contact</li>
  </ul>
  <div class="abs col-start">
    <div class="footer-heading">Getting Started</div>
    <ul class="footer-list footer-sub"><li>Demo</li><li>Documentation</li><li>Download</li></ul>
  </div>
  <div class="abs col-support">
    <div class="footer-heading">Support</div>
    <ul class="footer-list footer-sub"><li>Contact Us</li><li>Molveta Services</li><li>Molveta Support</li></ul>
  </div>
  <div class="abs col-follow">
    <div class="footer-heading">Follow Us</div>
    <div class="social-links">
      <a href="#" aria-label="Friendloop"></a><a href="#" aria-label="Chirpline"></a><a href="#" aria-label="Careerweave"></a><a href="#" aria-label="Blogmesa"></a>
    </div>
  </div>
  <div class="abs col-news">
    <div class="footer-heading">Newsletter Sign-up</div>
  </div>
  <div class="abs email-field">Email:</div>
  <a class="abs cta signup" href="#">Sign Up</a>
</footer>

<div class="legal-bar">© Copyright 2012 &nbsp;| &nbsp;Molveta &nbsp;| &nbsp;All rights reserved.</div>

</body>
</html>
```